Update our OBGYN business card look and info

We are an OBGYN office. Our logo is nice but would like to "woman" part of the logo to be a darker color, to contrast with the flower that surrounds it. Maybe make our practice name Harbor Bloom Care Clinic more feminine. Our practice caters to women only. All providers and staff are female.

Target Market(s)

Females 16-65.

Industry/Entity Type

Business

Contact Information for Business Card

See attached upload. The ONLY CHANGE to the information is DELETE the name Dorothy Kemplin, Midwife and REPLACE with Greta Poundsworth, Midwife

Logo Text

Harbor Bloom Care Clinic Obstetrics & Gynecology

Font styles to use
Serif
Script

Colors
85cae6
0692cd
33a6d7
85abd2
f59195
eea4c8
cadf82
fac994
d3a5cc

```html
<!DOCTYPE html>
<html lang="en">
<head>
<meta charset="utf-8">
<title>Harbor Bloom Care Clinic – Business Card</title>
<link rel="stylesheet" href="https://fonts.googleapis.com/css2?family=Cinzel:wght@400;500&family=Open+Sans:wght@400;600&display=swap">
<style>
  :root {
    --orange: #fb8c00;
    --green: #7fbf1f;
    --white: #ffffff;
    --ink: #3a3a3a;
    --page: #ece8e3;
  }
  * { box-sizing: border-box; margin: 0; padding: 0; }
  html, body {
    width: 1200px; height: 900px; overflow: hidden;
    background: var(--page);
  }
  .sheet {
    width: 1200px; height: 900px;
    display: flex; flex-direction: column; align-items: center; justify-content: center;
    gap: 40px;
  }
  .card {
    position: relative;
    width: 700px; height: 400px;
    overflow: hidden;
    box-shadow: 0 6px 18px rgba(0,0,0,0.18);
  }
  /* Front */
  .card-front { background: var(--orange); }
  .brand {
    position: absolute; left: 140px; top: 160px;
    display: flex; align-items: center; gap: 26px;
  }
  .brand-dot {
    width: 72px; height: 72px; border-radius: 50%;
    background: var(--white);
    flex: none;
  }
  .brand-name {
    font-family: "Open Sans", sans-serif;
    font-weight: 600;
    color: var(--white);
    font-size: 19px;
    line-height: 1.35;
  }
  .brand-name .practice { text-transform: uppercase; display: block; }
  .brand-name .specialty { display: block; font-size: 20px; }

  /* Back */
  .card-back { background: var(--white); }
  .wave { position: absolute; inset: 0; width: 700px; height: 400px; }
  .back-mark {
    position: absolute; right: 70px; top: 30px;
    width: 130px; height: 130px; border-radius: 50%;
    background: var(--orange);
  }
  .providers {
    position: absolute; left: 42px; top: 52px;
    list-style: none;
    font-family: "Cinzel", serif;
    font-weight: 500;
    color: var(--green);
    font-size: 22px;
    line-height: 36px;
  }
  .contacts {
    position: absolute; left: 42px; top: 220px;
    list-style: none;
    font-family: "Open Sans", sans-serif;
    color: var(--ink);
    font-size: 17px;
    line-height: 26px;
  }
  .contacts li { display: flex; align-items: center; gap: 10px; }
  .contacts svg { width: 15px; height: 15px; flex: none; }
  .address {
    position: absolute; right: 40px; top: 286px;
    text-align: right;
    font-family: "Open Sans", sans-serif;
    font-style: normal;
    color: var(--white);
    font-size: 14px;
    line-height: 21px;
  }
</style>
</head>
<body>
<main class="sheet">
  <section class="card card-front" aria-label="Card front">
    <div class="brand">
      <span class="brand-dot" aria-hidden="true"></span>
      <p class="brand-name">
        <span class="practice">Harbor Bloom Care Clinic</span>
        <span class="specialty">Obstetrics &amp; Gynecology</span>
      </p>
    </div>
  </section>

  <section class="card card-back" aria-label="Card back">
    <svg class="wave" viewBox="0 0 700 400" aria-hidden="true">
      <path d="M0,318 C170,362 340,330 520,228 C600,184 660,170 700,166 L700,178 C650,184 590,202 520,242 C340,345 170,378 0,340 Z" fill="var(--green)"/>
      <path d="M0,352 C170,390 350,355 530,250 C600,210 660,192 700,188 L700,400 L0,400 Z" fill="var(--orange)"/>
    </svg>
    <span class="back-mark" aria-hidden="true"></span>
    <ul class="providers">
      <li>Marian Ostrova, MD</li>
      <li>Celia Brandt, MD</li>
      <li>Greta Poundsworth, Midwife</li>
      <li>Naomi Fairweather, Midwife</li>
    </ul>
    <ul class="contacts">
      <li>
        <svg viewBox="0 0 16 16" aria-hidden="true"><path d="M3.5 1.5l2.5 0 1 3.5-1.7 1.3a9 9 0 0 0 4.4 4.4L11 9l3.5 1v2.5A2 2 0 0 1 12.5 14.5 11 11 0 0 1 1.5 3.5 2 2 0 0 1 3.5 1.5z" fill="var(--orange)"/></svg>
        555-301-4826
      </li>
      <li>
        <svg viewBox="0 0 16 16" aria-hidden="true"><rect x="1.5" y="5" width="13" height="9" rx="1.5" fill="var(--orange)"/><rect x="4" y="1.5" width="8" height="4.5" fill="var(--orange)"/><rect x="4.5" y="8" width="7" height="1.2" fill="var(--white)"/><rect x="4.5" y="10.5" width="7" height="1.2" fill="var(--white)"/></svg>
        555-301-4870
      </li>
      <li>
        <svg viewBox="0 0 16 16" aria-hidden="true"><circle cx="8" cy="8" r="6.5" fill="var(--orange)"/><path d="M1.5 8h13M8 1.5c-3 3.5-3 9.5 0 13M8 1.5c3 3.5 3 9.5 0 13" stroke="var(--white)" stroke-width="1" fill="none"/></svg>
        www.harborbloomcare.com
      </li>
    </ul>
    <address class="address">
      2480 Linden Ave.Ste 3B<br>
      Riverton,GA 30000-4417
    </address>
  </section>
</main>
</body>
</html>
```